The Perfect Business Card for PineHarbor

I am looking for a business card which beautifully incorporates my logo, reflects my business and looks special, elegant and clean.

```html
<!DOCTYPE html>
<html lang="en">
<head>
<meta charset="utf-8">
<title>PineHarbor Business Card</title>
<link rel="stylesheet" href="https://fonts.googleapis.com/css2?family=Open+Sans:wght@400;700&display=swap">
<style>
  :root {
    --backdrop: #ababab;
    --green: #7a9a44;
    --green-light: #7f9e48;
    --green-dark: #5b7630;
    --card-white: #ffffff;
    --leaf-teal: #a1bbb8;
    --leaf-sage: #d2e4bd;
    --leaf-mauve: #cdbcbb;
  }
  * { margin: 0; padding: 0; box-sizing: border-box; }
  html, body {
    width: 1200px;
    height: 1000px;
    overflow: hidden;
    background: var(--backdrop);
    font-family: "Open Sans", Arial, sans-serif;
  }
  .canvas {
    position: relative;
    width: 1200px;
    height: 1000px;
  }
  .card {
    position: absolute;
    left: 294px;
    width: 612px;
    height: 351px;
    border-radius: 24px;
    overflow: hidden;
  }
  .card-front {
    top: 125px;
    background: linear-gradient(90deg, var(--green) 0%, var(--green-light) 45%, var(--green-dark) 100%);
  }
  .card-back {
    top: 537px;
    background: var(--card-white);
  }
  .brand {
    position: absolute;
    display: flex;
    align-items: center;
    gap: 14px;
    font-weight: 400;
    letter-spacing: 0.5px;
  }
  .brand-dot {
    border-radius: 50%;
    flex: none;
  }
  .card-front .brand {
    left: 0;
    right: 0;
    top: 150px;
    justify-content: center;
    color: var(--card-white);
    font-size: 44px;
    line-height: 50px;
  }
  .card-front .brand-dot {
    width: 14px;
    height: 14px;
    background: var(--card-white);
  }
  .card-back .brand {
    right: 42px;
    top: 55px;
    color: var(--green);
    font-size: 30px;
    line-height: 36px;
    gap: 10px;
  }
  .card-back .brand-dot {
    width: 10px;
    height: 10px;
    background: var(--green);
  }
  .foliage {
    position: absolute;
    left: 26px;
    top: 94px;
    width: 256px;
    height: 232px;
    border-radius: 40% 55% 45% 50%;
    background: linear-gradient(120deg, var(--leaf-mauve) 0%, var(--leaf-teal) 40%, var(--leaf-sage) 80%);
    opacity: 0.85;
  }
  .contact {
    position: absolute;
    right: 44px;
    top: 146px;
    text-align: right;
    color: var(--green);
  }
  .contact-name {
    font-weight: 700;
    font-size: 21px;
    line-height: 30px;
    margin-bottom: 18px;
  }
  .contact-line {
    font-size: 19px;
    line-height: 30px;
  }
  .contact-address {
    font-size: 19px;
    line-height: 30px;
    margin-top: 32px;
  }
</style>
</head>
<body>
<main class="canvas">
  <section class="card card-front">
    <div class="brand">
      <span class="brand-dot"></span>
      <span class="brand-name">PineHarbor</span>
    </div>
  </section>

  <section class="card card-back">
    <div class="brand">
      <span class="brand-dot"></span>
      <span class="brand-name">PineHarbor</span>
    </div>
    <div class="foliage" role="img" aria-label="Soft illustrated leaves in teal, sage green and dusty mauve"></div>
    <div class="contact">
      <p class="contact-name">Dr. Maren Holtby</p>
      <p class="contact-line">+41 (0)76 000 12 34</p>
      <p class="contact-line">info@pineharbor.ch</p>
      <p class="contact-address">Lindenweg 7, 8004 Zürich</p>
    </div>
  </section>
</main>
</body>
</html>
```